Oven Cleaning Business owner needs business card design

Hi there,
Would like for a business card to be designed for myself, the owner of a professional oven cleaning business on the Sunshine Coast.
Would like it to look sleek, and modern-ish. Bit creative is encouraged too.
Include following:
Name/title: Corin ter Haghe, Owner
Phone number: 1300 482 916
Email: info@hearthshinecrew.com.au
Website: www.hearthshinecrew.com.au

```html
<!DOCTYPE html>
<html lang="en">
<head>
<meta charset="utf-8">
<title>Hearthshine Crew — Business Card</title>
<link rel="stylesheet" href="https://fonts.googleapis.com/css2?family=Montserrat:wght@600&family=Quicksand:wght@400;500&display=swap">
<style>
  :root {
    --stage: #2b2f35;
    --navy: #053a55;
    --teal-deep: #0a6f7a;
    --teal-glow: #0f9a98;
    --cyan: #1ad9dd;
    --cyan-soft: #5fe3e6;
    --teal-text: #0e8a92;
    --ink: #111416;
    --grey: #7b8084;
    --paper: #ffffff;
  }
  * { box-sizing: border-box; margin: 0; padding: 0; }
  html, body { width: 1200px; height: 1143px; overflow: hidden; }
  body {
    background: var(--stage);
    position: relative;
    font-family: "Quicksand", sans-serif;
  }
  .card {
    position: absolute;
    top: 425px;
    width: 512px;
    height: 292px;
    overflow: hidden;
  }
  .card-front {
    left: 71px;
    background: radial-gradient(ellipse 60% 75% at 48% 52%, var(--teal-glow) 0%, var(--teal-deep) 40%, var(--navy) 100%);
  }
  .card-back {
    left: 595px;
    background: var(--paper);
  }

  .art-panel {
    position: absolute;
    top: 0;
    height: 292px;
  }
  .card-front .art-panel {
    right: 0;
    width: 120px;
    background: linear-gradient(180deg, var(--cyan-soft) 0%, var(--cyan) 100%);
  }
  .card-back .art-panel {
    left: 0;
    width: 130px;
    background: linear-gradient(180deg, var(--cyan-soft) 0%, var(--cyan) 100%);
  }

  .brand {
    display: flex;
    align-items: center;
    gap: 10px;
    font-family: "Montserrat", sans-serif;
    font-weight: 600;
    letter-spacing: 0.04em;
    text-transform: uppercase;
    line-height: 1;
    white-space: nowrap;
  }
  .brand-dot { border-radius: 50%; background: var(--cyan); flex: none; }
  .card-front .brand {
    position: absolute;
    left: 38px; top: 118px;
    font-size: 24px;
    color: var(--cyan);
  }
  .card-front .brand-dot { width: 40px; height: 40px; }
  .card-back .brand {
    position: absolute;
    right: 28px; top: 40px;
    font-size: 19px;
    color: var(--ink);
  }
  .card-back .brand-dot { width: 34px; height: 34px; }

  .person {
    position: absolute;
    right: 21px; top: 124px;
    text-align: right;
  }
  .person-name {
    font-family: "Montserrat", sans-serif;
    font-weight: 600;
    font-size: 20px;
    color: var(--teal-text);
  }
  .person-name .surname { color: var(--ink); }
  .person-title {
    font-size: 15px;
    color: var(--grey);
    margin-top: 2px;
  }
  .contact-list {
    position: absolute;
    right: 20px; top: 203px;
    list-style: none;
    text-align: right;
    font-size: 13.5px;
    color: var(--ink);
  }
  .contact-list li {
    display: flex;
    justify-content: flex-end;
    align-items: center;
    gap: 8px;
    height: 18.5px;
  }
  .contact-icon { width: 12px; height: 12px; fill: var(--teal-text); flex: none; }
</style>
</head>
<body>

<section class="card card-front" aria-label="Card front">
  <div class="brand"><span class="brand-dot"></span>Hearthshine Crew</div>
  <div class="art-panel" role="img" aria-label="Brand illustration area: cleaning graphic with sparkles in cyan and black"></div>
</section>

<section class="card card-back" aria-label="Card back">
  <div class="art-panel" role="img" aria-label="Brand illustration area: cleaning graphic continued in cyan and black"></div>

  <div class="brand"><span class="brand-dot"></span>Hearthshine Crew</div>

  <div class="person">
    <p class="person-name">Corin ter <span class="surname">Haghe</span></p>
    <p class="person-title">Owner</p>
  </div>

  <ul class="contact-list">
    <li>1300 482 916
      <svg class="contact-icon" viewBox="0 0 24 24" aria-hidden="true"><path d="M6.6 10.8a15.1 15.1 0 0 0 6.6 6.6l2.2-2.2a1 1 0 0 1 1-.25 11.4 11.4 0 0 0 3.6.57 1 1 0 0 1 1 1V20a1 1 0 0 1-1 1A17 17 0 0 1 3 4a1 1 0 0 1 1-1h3.5a1 1 0 0 1 1 1c0 1.25.2 2.45.57 3.6a1 1 0 0 1-.25 1z"/></svg>
    </li>
    <li>info@hearthshinecrew.com.au
      <svg class="contact-icon" viewBox="0 0 24 24" aria-hidden="true"><path d="M2 5h20v14H2z M2 5l10 8 10-8" fill="var(--teal-text)" stroke="#fff" stroke-width="1.5"/></svg>
    </li>
    <li>www.hearthshinecrew.com.au
      <svg class="contact-icon" viewBox="0 0 24 24" aria-hidden="true"><circle cx="12" cy="12" r="10"/><path d="M2 12h20M12 2c3 3 3 17 0 20M12 2c-3 3-3 17 0 20" stroke="#fff" stroke-width="1.5" fill="none"/></svg>
    </li>
  </ul>
</section>

</body>
</html>
```